Title loan company needs a postcard design, front/back, for marketing to former customers

We need a clean postcard design for the purpose of a mailer to engage former customers to come in and take out a loan.
We want to reinforce the benefits of doing business with us and give them an incentive offer to borrow money with us again.

The special offer: $50 Bonus Cash on your next loan

Some points or benefits we offer:
-No Credit Check
-Instant Approval
-Easy Payments
-15 Minute Loans
-Coin Steady Approved-I am providing this as a image for a state association we are members of. You may use the logo or use it as a benefit.
-Satisfaction Guarantee-I am providing this as an image as a guarantee. I personally feel that this should image should be used as a reinforcement of said guarantee.

The loan product is know as a title loan. The customer pledges the car title to their vehicle as security for the loan in exchange for cash.

Front and back of the card should have a call to action.
Looking for a clean design for the front and back of the postcard.
Back of the card should have a space for postage stamp, or indicia, and enough room for a mailing label

Visit our website for any additional information that you may have or ask me directly.

pinemarkfunding.com

Hex color codes of the logo should you incorporate this into the design.
Light Green in Logo: #b7dc78
Dark Green in Logo: #00953a
Yellow in Logo: #ffdd00

I am attaching our logo, the coin steady seal, and the guarantee shield.
I am also attaching templates for illustrator, photoshop, acrobat. Use one of the templates as it has the correct bleeds for my printer. If you need another template let me know.

Reason: I am extending the deadline but I only really need a day before i choose the final design. Had a technical error that prevents me from getting this done & it should be rectified by the end of the day today?

Target Market(s)

25-54
Male/Female = 50% Split

Industry/Entity Type

Loan

Font styles to use
Serif
Sans Serif

Requirements
Must have
• Clean Design, Call to Action, Draw attention to special offer
Nice to have
• Use of some of the colors in logo, hex color codes are in description, for branding purposes! Not a requirement! Let see what you bring to the table.

```html
<!DOCTYPE html>
<html lang="en">
<head>
<meta charset="utf-8">
<title>Pinemark Funding – Postcard Front and Back</title>
<link rel="stylesheet" href="https://fonts.googleapis.com/css2?family=Anton&family=Open+Sans:wght@400;600;700;800&family=Roboto+Condensed:ital,wght@0,700;1,700&display=swap">
<style>
  :root{
    --green:#00953a;
    --green-deep:#0a7a34;
    --green-light:#b7dc78;
    --yellow:#ffdd00;
    --ink:#222222;
    --white:#ffffff;
    --page:#e9e9e9;
    --rule:#bdbdbd;
    --corner:#1b1b1b;
    --wash:#eef3e6;
  }
  *{margin:0;padding:0;box-sizing:border-box}
  html,body{width:816px;height:1200px;overflow:hidden;background:var(--page)}
  body{position:relative;font-family:"Open Sans",Arial,sans-serif;color:var(--ink)}

  .postcard{position:absolute;left:45px;width:726px;height:513px;background:var(--white);overflow:hidden;box-shadow:0 4px 14px rgba(0,0,0,.25)}
  .postcard--front{top:53px}
  .postcard--back{top:629px}
  .postcard__art{position:absolute;left:0;top:0}

  .brand{position:absolute;display:flex;align-items:center;gap:8px;font-weight:700;color:var(--green-deep);line-height:1;white-space:nowrap}
  .brand__dot{width:20px;height:20px;border-radius:50%;background:var(--yellow);flex:none}
  .brand--front{left:24px;top:62px;font-size:22px}
  .brand--back{left:404px;top:72px;font-size:20px}

  .web-bar{position:absolute;left:398px;top:17px;width:328px;height:38px;background:var(--green);clip-path:polygon(22px 0,100% 0,100% 100%,0 100%);color:var(--white);display:flex;align-items:center;padding-left:50px;font-size:18px;gap:9px}
  .web-bar svg,.footer-bar svg{flex:none}

  .offer__amount{position:absolute;left:36px;top:188px;font-family:"Anton",Impact,sans-serif;font-size:90px;color:var(--green);line-height:1}
  .offer__bonus{position:absolute;left:185px;top:194px;font-weight:800;font-size:36px;line-height:.95;color:var(--ink);white-space:nowrap}
  .offer__on{position:absolute;left:36px;top:266px;font-weight:800;font-size:34px;line-height:1.2;color:#111;white-space:nowrap}
  .offer__next{position:absolute;left:36px;top:302px;font-weight:800;font-size:44px;line-height:1.1;color:var(--green);white-space:nowrap}

  .benefits-bar{position:absolute;left:0;top:367px;width:280px;height:28px;background:var(--green);clip-path:polygon(0 0,91% 0,100% 100%,0 100%);color:var(--yellow);font-weight:800;font-size:16px;padding-left:38px;line-height:28px}
  .benefits{position:absolute;left:36px;top:408px;display:grid;grid-template-columns:150px 150px;row-gap:5px;list-style:none;font-family:"Roboto Condensed",Arial,sans-serif;font-style:italic;font-weight:700;font-size:17px;line-height:22px;color:var(--green-deep);white-space:nowrap}
  .benefits li::before{content:"✓ ";color:#111;font-style:normal}

  .call-bar{position:absolute;left:0;top:466px;width:353px;height:47px;background:var(--yellow);clip-path:polygon(0 0,94% 0,100% 100%,0 100%);font-weight:800;font-size:27px;padding-left:36px;line-height:47px;color:#111;white-space:nowrap}

  .photo{position:absolute;border-radius:50%}
  .photo--gifts{left:326px;top:180px;width:144px;height:144px;border:6px solid var(--green);background:radial-gradient(circle,#f6d7c8,#e7e2ee);box-shadow:0 0 0 3px #fff inset}
  .seal{left:324px;top:312px;width:116px;height:116px;border:6px solid var(--green);background:var(--white);display:flex;align-items:center;justify-content:center}
  .seal span{width:76px;height:76px;border-radius:50%;background:var(--green-light);display:block}

  .back-notes{position:absolute;left:28px;top:30px;list-style:none;font-size:14px;line-height:21px;color:#333;white-space:nowrap}
  .back-notes li{position:relative;padding-left:22px;margin-bottom:7px}
  .back-notes li::before{content:"✓";position:absolute;left:0;color:var(--green)}
  .product-note{position:absolute;left:50px;top:270px;color:var(--green);font-weight:700;font-size:15px;line-height:23px;white-space:nowrap}
  .product-note strong{font-size:19px;font-weight:800;display:block;line-height:29px}
  .photo--gold{left:324px;top:182px;width:144px;height:144px;border:6px solid var(--green);background:radial-gradient(circle,#f3d36a,#b8860b 60%,#fff 61%)}
  .photo--keys{left:314px;top:324px;width:120px;height:120px;border:6px solid var(--green);background:radial-gradient(circle,#c9cdb8,#f4f4f0 70%)}
  .social{position:absolute;left:203px;top:422px;display:flex;gap:10px}
  .social span{width:29px;height:29px;border-radius:50%;background:var(--green)}
  .stamp-box{position:absolute;left:620px;top:32px;width:74px;height:77px;border:1px solid #999}
  .address-lines{position:absolute;left:495px;top:272px;width:199px}
  .address-lines span{display:block;height:1px;background:var(--rule);margin-bottom:33px}
  .footer-bar{position:absolute;left:0;top:465px;height:48px;width:353px;background:var(--green);clip-path:polygon(0 0,94% 0,100% 100%,0 100%);color:var(--white);display:flex;align-items:center;gap:10px;padding-left:34px;font-size:19px;white-space:nowrap}
</style>
</head>
<body>

<section class="postcard postcard--front" aria-label="Postcard front">
  <svg class="postcard__art" width="726" height="513" viewBox="0 0 726 513">
    <defs>
      <linearGradient id="photoTone" x1="0" y1="0" x2="1" y2="1">
        <stop offset="0" stop-color="#d9c4ad"/><stop offset=".5" stop-color="#9a7a62"/><stop offset="1" stop-color="#6b4d36"/>
      </linearGradient>
    </defs>
    <rect x="320" y="0" width="406" height="513" fill="url(#photoTone)" role="img" aria-label="Photo of a smiling couple shaking hands with a loan officer across a desk"/>
    <path d="M0 0 H281 C350 140 380 330 340 513 H0 Z" fill="var(--white)"/>
    <path d="M281 0 H305 C375 140 405 330 365 513 H340 C380 330 350 140 281 0 Z" fill="var(--yellow)"/>
    <path d="M305 0 H330 C400 140 432 330 392 513 H365 C405 330 375 140 305 0 Z" fill="var(--green)"/>
    <path d="M0 112 C90 165 220 150 320 60 C230 180 90 195 0 142 Z" fill="var(--green)"/>
    <path d="M0 142 C90 195 230 180 320 60 C250 205 90 225 0 172 Z" fill="var(--wash)"/>
    <path d="M726 470 V513 H672 Z" fill="var(--corner)"/>
    <path d="M654 430 l24 -10 l24 10 v26 c0 18 -12 28 -24 34 c-12 -6 -24 -16 -24 -34 Z" fill="var(--green-light)" stroke="#8a9c7e" stroke-width="3"/>
  </svg>

  <div class="brand brand--front"><span class="brand__dot"></span>Pinemark Funding</div>

  <div class="web-bar">
    <svg width="16" height="16" viewBox="0 0 16 16" fill="none" stroke="#fff" stroke-width="1.4"><circle cx="8" cy="8" r="7"/><ellipse cx="8" cy="8" rx="3" ry="7"/><path d="M1 8h14"/></svg>
    pinemarkfunding.com
  </div>

  <div class="offer__amount">$50</div>
  <div class="offer__bonus">BONUS<br>CASH</div>
  <div class="offer__on">on your</div>
  <div class="offer__next">NEXT LOAN</div>

  <div class="benefits-bar">BENEFITS WE OFFER:</div>
  <ul class="benefits">
    <li>No Credit Check</li><li>Instant Approval</li>
    <li>Easy Payments</li><li>15 Minute Loans</li>
  </ul>
  <div class="call-bar">CALL 0123 456 789</div>

  <div class="photo photo--gifts" role="img" aria-label="Gift cards offered as bonus cash"></div>
  <div class="photo seal" role="img" aria-label="Coin Steady Approved seal"><span></span></div>
</section>

<section class="postcard postcard--back" aria-label="Postcard back">
  <svg class="postcard__art" width="726" height="513" viewBox="0 0 726 513">
    <path d="M292 0 H316 C402 150 420 330 378 513 H352 C392 330 376 150 292 0 Z" fill="var(--yellow)"/>
    <path d="M316 0 H340 C428 150 446 330 404 513 H378 C420 330 402 150 316 0 Z" fill="var(--green)"/>
    <path d="M240 160 C295 230 305 330 275 420 C300 300 285 225 240 160 Z" fill="var(--wash)"/>
    <path d="M726 470 V513 H672 Z" fill="var(--corner)"/>
    <path d="M654 430 l24 -10 l24 10 v26 c0 18 -12 28 -24 34 c-12 -6 -24 -16 -24 -34 Z" fill="var(--green-light)" stroke="#8a9c7e" stroke-width="3"/>
  </svg>

  <ul class="back-notes">
    <li>Coin Steady Approved-I am<br>providing this as a image for a<br>state association we are members<br>of. You may use the logo or use<br>it as a benefit.</li>
    <li>Satisfaction Guarantee-I am providing<br>this as an image as a guarantee.<br>I personally feel that this should image<br>should be used as a reinforcement<br>of said guarantee.</li>
  </ul>

  <div class="brand brand--back"><span class="brand__dot"></span>Pinemark Funding</div>
  <div class="stamp-box"></div>
  <div class="address-lines"><span></span><span></span><span></span></div>

  <p class="product-note">The loan product is know<strong>AS A TITLE LOAN.</strong>The customer pledges the<br>car title to their vehicle<br>as security for the loan<br>in exchange for cash.</p>

  <div class="photo photo--gold" role="img" aria-label="Stacked gold bars"></div>
  <div class="photo photo--keys" role="img" aria-label="Car key resting on banknotes"></div>

  <div class="social"><span></span><span></span><span></span></div>

  <div class="footer-bar">
    <svg width="18" height="18" viewBox="0 0 16 16" fill="none" stroke="#fff" stroke-width="1.4"><circle cx="8" cy="8" r="7"/><ellipse cx="8" cy="8" rx="3" ry="7"/><path d="M1 8h14"/></svg>
    pinemarkfunding.com
  </div>
</section>

</body>
</html>
```